Capability statement for an Electrical Business based in Sydney Australia

The aim for the Capability statement is for us to look more professional when we meet someone or after cold calling and have to send them our business details.
Need something simple, efficient and to the point.

It should have the following content
- Our mission (details can be as attached PDF)
- Areas we service (this can be a google map of areas we service but basically the areas are
Metro Sydney with our work centralised around the Norwest, Hills, Inner west and Epping area)
- List of services we provide (as PDF)
- Details about us; who we are, contact details, licenses (as PDF)
- Why they should choose us
(As pdf)

Right now, we're just after a nice format we're happy with, the details we are happy to provide with once we have a design in mind.

I've attached our current existing capability statement and what our details are. Also, our website is
https://themardenfield.com.au/

Thanks in advance!

• Should not be complicated for the reader

```html
<!DOCTYPE html>
<html lang="en">
<head>
<meta charset="utf-8">
<title>The Marden Field – Capability Statement</title>
<link rel="stylesheet" href="https://fonts.googleapis.com/css2?family=Bebas+Neue&family=Catamaran:wght@400;500;600;700&display=swap">
<style>
  :root{
    --red:#dc3a2c;
    --red-line:#d9342a;
    --white:#ffffff;
    --ink:#1f1f1f;
    --bg:#e8e5e1;
    --photo-dark:#161a20;
    --photo-grey:#6c6a63;
    --photo-green:#2f4a26;
  }
  *{box-sizing:border-box;margin:0;padding:0}
  html,body{width:1200px;height:750px;overflow:hidden;background:var(--bg)}
  body{position:relative;font-family:"Catamaran",sans-serif;color:var(--ink)}
  .page{position:absolute;top:99px;width:427px;height:552px;background:var(--white);overflow:hidden;box-shadow:0 6px 18px rgba(0,0,0,.18)}
  .page--front{left:150px}
  .page--back{left:626px}

  .side{position:absolute;left:0;width:159px;background:var(--red);color:var(--white);text-align:center}
  .page--front .side{top:0;bottom:0}
  .page--back .side{top:148px;bottom:0}

  .brand{font-weight:700;font-size:15px;line-height:16px;letter-spacing:1.5px;color:var(--white);text-transform:uppercase}
  .page--front .brand{position:absolute;top:50px;left:0;right:0}
  .side-rule{position:absolute;top:115px;left:52px;width:50px;height:1.5px;background:var(--white)}
  .side h2{font-weight:500;font-size:14px;line-height:16px;text-transform:uppercase}
  .who h2{position:absolute;top:141px;left:0;right:0}
  .who-text{position:absolute;top:192px;left:26px;right:26px;font-size:7.8px;line-height:10.4px}
  .who-text p+p{margin-top:10px}
  .contact{position:absolute;top:406px;left:0;right:0;font-size:7.8px;line-height:11px}
  .contact svg{display:block;margin:0 auto 2px}
  .contact .phone-icon{margin-top:8px}

  .hero{position:absolute;top:0;left:159px;right:0;height:181px;background:radial-gradient(circle at 78% 40%,#5b5548 0,#2b2b2c 30%,var(--photo-dark) 70%)}
  .hero-title{position:absolute;left:26px;top:78px;font-family:"Bebas Neue",sans-serif;font-size:43px;line-height:40px;color:var(--white)}

  .tab{position:absolute;left:159px;right:0}
  .tab svg{position:absolute;left:0;top:0}
  .tab span{position:absolute;left:23px;color:var(--white);font-weight:500;text-transform:uppercase;white-space:nowrap}
  .tab--mission{top:194px;height:20px}
  .tab--mission span{top:1px;font-size:13.5px}
  .tab--values{top:267px;height:21px}
  .tab--values span{top:1px;font-size:13.5px}
  .tab--services{top:368px;height:38px}
  .tab--services span{top:5px;font-size:11.8px;line-height:14px}

  .mission-text{position:absolute;top:224px;left:183px;right:27px;font-size:7.8px;line-height:10.4px;text-align:justify}

  .values{position:absolute;top:298px;left:159px;right:0;height:60px}
  .value{position:absolute;width:64px;margin-left:-32px;text-align:center;font-size:7.6px;line-height:10.4px}
  .value svg{display:block;margin:0 auto 4px}

  .services{position:absolute;top:418px;left:159px;right:0;font-size:6.7px;line-height:8.2px}
  .services ul{position:absolute;list-style:none}
  .services .col-a{left:20px;width:120px}
  .services .col-b{left:151px;width:112px}
  .services li{position:relative;padding-left:17px;margin-bottom:5.6px}
  .services li svg{position:absolute;left:0;top:0}

  .back-hero-left{position:absolute;top:0;left:0;width:159px;height:148px;background:linear-gradient(160deg,#7a7870,var(--photo-grey) 55%,#57564f)}
  .page--back .brand{position:absolute;top:71px;left:0;width:159px;text-align:center}
  .back-hero-right{position:absolute;top:0;left:159px;right:0;height:148px;background:radial-gradient(circle at 80% 30%,#5b6f4c 0,#3c5a30 30%,var(--photo-green) 60%,#1f3219)}
  .why-title{position:absolute;left:26px;top:60px;font-family:"Bebas Neue",sans-serif;font-size:39px;line-height:36px;color:var(--white)}

  .licenses h2{position:absolute;top:176px;left:0;right:0}
  .licenses-text{position:absolute;top:196px;left:0;right:0;font-weight:600;font-size:8.4px;line-height:10.6px}
  .licenses-text p{margin-bottom:3.5px}
  .licenses-text .gap{margin-top:11px}
  .areas h2{position:absolute;top:323px;left:0;right:0}
  .areas-text{position:absolute;top:363px;left:20px;right:20px;font-weight:600;font-size:8.4px;line-height:10.4px}
  .map{position:absolute;left:25px;top:412px;width:110px;height:110px;border-radius:50%;border:2px solid var(--white);background:radial-gradient(circle at 62% 55%,#c9d9ea 0,#e6e2d4 35%,#d6e4c8 70%,#bfd3e8)}

  .reasons{position:absolute;top:179px;left:185px;right:27px}
  .reason{margin-bottom:13.6px}
  .reason h3{font-weight:500;font-size:9.2px;line-height:10.4px;text-transform:uppercase}
  .reason p{font-size:7.6px;line-height:10.4px;text-align:justify}

  .site{position:absolute;top:525px;left:208px;font-size:7.8px}
  .site-rule{position:absolute;top:530px;left:124px;width:74px;height:1px;background:var(--red-line)}
</style>
</head>
<body>

<section class="page page--front">
  <aside class="side">
    <div class="brand">The Marden<br>Field</div>
    <div class="side-rule"></div>
    <div class="who">
      <h2>Who<br>We Are</h2>
      <div class="who-text">
        <p>The Marden Field is a growing Electrical maintenance company based in the Inner West.</p>
        <p>We are established on sound service principles with honesty, communication, and respect at the forefront of every team member.</p>
        <p>We strive for openness, trust, and accountability and we are in the business of providing solutions to help others. We see ourselves as an extension of your team.</p>
      </div>
    </div>
    <div class="contact">
      <svg width="9" height="6" viewBox="0 0 9 6"><rect x=".5" y=".5" width="8" height="5" fill="none" stroke="#fff"/><path d="M.5 .5 4.5 3.5 8.5 .5" fill="none" stroke="#fff"/></svg>
      <div>services@themardenfield.com.au</div>
      <svg class="phone-icon" width="8" height="8" viewBox="0 0 8 8"><path d="M1.5 0.5 3 2.5 2 3.5Q3 5.5 4.5 6L5.5 5 7.5 6.5 6.5 7.8Q2.5 7.5 0.3 1.5Z" fill="#fff"/></svg>
      <div>Daniel: 0400 182 736</div>
      <div>Bruce: 0412 559 804</div>
    </div>
  </aside>

  <div class="hero" role="img" aria-label="Photo of hanging vintage filament light bulbs on a dark background"></div>
  <h1 class="hero-title hero-title-pos" style="left:185px">Capability<br>Statement</h1>

  <div class="tab tab--mission">
    <svg width="268" height="20" viewBox="0 0 268 20"><path d="M0 0H107L117 18H268V20H0Z" fill="var(--red)"/></svg>
    <span>Mission</span>
  </div>
  <p class="mission-text">Dedicate ourselves to providing world class service to anyone in need, based on honesty, communication and respect.</p>

  <div class="tab tab--values">
    <svg width="268" height="21" viewBox="0 0 268 21"><path d="M0 0H148L158 16H268V21H0Z" fill="var(--red)"/></svg>
    <span>Core Values</span>
  </div>
  <div class="values">
    <div class="value" style="left:46px">
      <svg width="18" height="20" viewBox="0 0 18 20"><path d="M9 0 18 3V9Q18 16 9 20 0 16 0 9V3Z" fill="var(--red)"/><path d="M5 10 8 13 13 7" fill="none" stroke="#fff" stroke-width="2"/></svg>
      Safety<br>and Security<br>is priority
    </div>
    <div class="value" style="left:99px">
      <svg width="22" height="20" viewBox="0 0 22 20"><path d="M3 18 9 8 13 8 19 18" fill="none" stroke="var(--red)" stroke-width="1.6"/><path d="M6 13 11 9 16 13" fill="none" stroke="var(--red)" stroke-width="1.6"/><path d="M11 1V4M5 3 7 5M17 3 15 5" stroke="var(--red)" stroke-width="1.2"/></svg>
      Support<br>when you<br>need it most
    </div>
    <div class="value" style="left:158px">
      <svg width="18" height="20" viewBox="0 0 18 20"><circle cx="9" cy="7" r="6.5" fill="var(--red)"/><circle cx="9" cy="7" r="3" fill="#fff"/><path d="M4 11 2 19 5 17 7 19 8 13M14 11 16 19 13 17 11 19 10 13" fill="var(--red)"/></svg>
      Service<br>with an over-<br>the-top WOW
    </div>
    <div class="value" style="left:218px">
      <svg width="20" height="20" viewBox="0 0 20 20"><path d="M10 1A8.5 8 0 1 1 6 16L4 19 4.5 14.5A8.5 8 0 0 1 10 1Z" fill="none" stroke="var(--red)" stroke-width="1.6"/><path d="M10 4.5 11.3 7.7 14.6 7.9 12 10 12.9 13.3 10 11.5 7.1 13.3 8 10 5.4 7.9 8.7 7.7Z" fill="var(--red)"/></svg>
      Satisfaction<br>with loyalty<br>and integrity
    </div>
  </div>

  <div class="tab tab--services">
    <svg width="268" height="38" viewBox="0 0 268 38"><path d="M0 0H228L250 33H268V38H0Z" fill="var(--red)"/></svg>
    <span>Brief list of the most<br>common services we provide</span>
  </div>
  <div class="services">
    <ul class="col-a">
      <li><svg width="10" height="10" viewBox="0 0 10 10"><circle cx="5" cy="5" r="4.2" fill="none" stroke="var(--red)" stroke-width="1.2"/><path d="M5 2.5V5H7" fill="none" stroke="var(--red)"/></svg>24/7 Emergency service</li>
      <li><svg width="10" height="10" viewBox="0 0 10 10"><circle cx="5" cy="5" r="4.2" fill="none" stroke="var(--red)" stroke-width="1.2"/><path d="M5 7.5V3M3 5 5 3 7 5" fill="none" stroke="var(--red)"/></svg>Switchboard UPGRADE<br>and REPAIRS</li>
      <li><svg width="10" height="10" viewBox="0 0 10 10"><circle cx="5" cy="4" r="2.6" fill="var(--red)"/><rect x="4" y="7" width="2" height="2" fill="var(--red)"/></svg>Light fitting installations</li>
      <li><svg width="10" height="10" viewBox="0 0 10 10"><rect x="1" y="1" width="8" height="8" fill="var(--red)"/><rect x="3" y="3" width="1.2" height="2.5" fill="#fff"/><rect x="5.8" y="3" width="1.2" height="2.5" fill="#fff"/></svg>Powerpoint installations</li>
      <li><svg width="10" height="10" viewBox="0 0 10 10"><path d="M6 0 1.5 5.5H4.5L3.5 10 8.5 4H5.5Z" fill="var(--red)"/></svg>Surge device installations</li>
      <li><svg width="10" height="12" viewBox="0 0 10 12"><rect x="3.5" y="0.5" width="3" height="7" rx="1.5" fill="none" stroke="var(--red)"/><circle cx="5" cy="9" r="2.3" fill="var(--red)"/></svg>Testing and servicing electric<br>hot water systems</li>
      <li><svg width="11" height="10" viewBox="0 0 11 10"><circle cx="5.5" cy="5" r="1.6" fill="var(--red)"/><path d="M3 2Q1 5 3 8M8 2Q10 5 8 8" fill="none" stroke="var(--red)"/></svg>Smoke Alarm installation<br>with compliance certificate</li>
    </ul>
    <ul class="col-b">
      <li><svg width="11" height="10" viewBox="0 0 11 10"><path d="M1 7V4.5L2.5 2H8.5L10 4.5V7Z" fill="var(--red)"/><circle cx="3" cy="7.5" r="1.2" fill="var(--red)"/><circle cx="8" cy="7.5" r="1.2" fill="var(--red)"/></svg>Electric Vehicle<br>charging stations</li>
      <li><svg width="10" height="10" viewBox="0 0 10 10"><circle cx="5" cy="5" r="1.3" fill="var(--red)"/><ellipse cx="5" cy="2" rx="1.6" ry="2" fill="var(--red)"/><ellipse cx="2.2" cy="7" rx="2" ry="1.6" fill="var(--red)"/><ellipse cx="7.8" cy="7" rx="2" ry="1.6" fill="var(--red)"/></svg>Ceiling and Exhaust fan<br>installations with roof<br>and wall venting</li>
      <li><svg width="10" height="10" viewBox="0 0 10 10"><circle cx="5" cy="5" r="3.6" fill="none" stroke="var(--red)" stroke-width="2" stroke-dasharray="2 1.2"/><circle cx="5" cy="5" r="1.3" fill="var(--red)"/></svg>Appliance installations</li>
      <li><svg width="11" height="10" viewBox="0 0 11 10"><rect x=".5" y="1" width="10" height="6.5" fill="var(--red)"/><rect x="3.5" y="8.2" width="4" height="1" fill="var(--red)"/></svg>TV, DATA and FREE TO<br>AIR Aerial installations</li>
      <li><svg width="10" height="10" viewBox="0 0 10 10"><circle cx="4" cy="4" r="3" fill="none" stroke="var(--red)" stroke-width="1.3"/><path d="M6.2 6.2 9.2 9.2" stroke="var(--red)" stroke-width="1.5"/></svg>Fault finding</li>
    </ul>
  </div>
</section>

<section class="page page--back">
  <div class="back-hero-left" role="img" aria-label="Blurred photo of a garden path"></div>
  <div class="brand">The Marden<br>Field</div>
  <div class="back-hero-right" role="img" aria-label="Photo of a garden lamp among green shrubs"></div>
  <h1 class="why-title" style="left:185px">Why choose<br>The Marden Field</h1>

  <aside class="side">
  </aside>
  <div class="side licenses" style="top:0;bottom:auto;background:none;width:159px;height:0">
    <h2>Licenses</h2>
    <div class="licenses-text">
      <p>Electrical License Number<br>The Marden Field<br>Pty Ltd - 518260C</p>
      <p>Daniel - 447102C</p>
      <p>Bruce - 362915C</p>
      <p class="gap">ABN: 5128 0463 911</p>
      <p class="gap">Public Liability<br>$20,000,000</p>
    </div>
  </div>
  <div class="side areas" style="top:0;bottom:auto;background:none;width:159px;height:0">
    <h2>Areas We<br>Service</h2>
    <p class="areas-text">Metro Sydney with our work centralised around the Norwest, Hills, Inner West and Epping Area</p>
  </div>
  <div class="map" role="img" aria-label="Street map of metropolitan Sydney showing the service area"></div>

  <div class="reasons">
    <div class="reason">
      <h3>Support when you need it most</h3>
      <p>The Field provides around the clock assistance, whether during normal business hours or emergencies we are focused on providing solutions for our clients.</p>
    </div>
    <div class="reason">
      <h3>Fast and responsive team with a<br>direct contact</h3>
      <p>The Field treats every one of our clients as a VIP. We pride ourselves on being able to provide a quick turn around for all our jobs. We make the whole process smooth, from booking the job to attending and completion.</p>
    </div>
    <div class="reason">
      <h3>Satisfaction with loyalty and integrity</h3>
      <p>We value our transparency and communication skills to deliver an outstanding performance which reflects our happy customer base.</p>
    </div>
    <div class="reason">
      <h3>We provide courtesy calls</h3>
      <p>The appointment will be confirmed the day before and our technicians will call you half an hour in advance on approach to the job.</p>
    </div>
    <div class="reason">
      <h3>Licensed and insured technicians</h3>
      <p>All our technicians are experts of their field, with the relevant equipment, knowledge and licenses to carry out our duties.</p>
    </div>
  </div>

  <div class="site-rule"></div>
  <div class="site">themardenfield.com.au</div>
</section>

</body>
</html>
```